Design of Premium Instant Tea Packaging (Tea in 3 seconds)

We need a fully packaging and sachets design for our new premium instant tea (Tea in 3 seconds) collection to our new brand BrimLeaf. The company is based in Norway and are founded by two Norwegian with a passion for tea and with a mission to share our passion in a faster and easier manner.

We would like a design that gives an exclusive, healthy, tasty and warm feeling. The design should communicate instant tea of high quality.

The tea is one of the first premium instant tea on the market and should give the customer a feeling of exclusive innovation, A new tea company is in town. We don't want to be similar to other old granny tea companies and we hate tea bags :P.

About our products. We offer two different Flavours:
Brim Hibiscus and Brim Lemon. The Brim Hibiscus is sweet and red as blood in its color.

We are looking for a universal design where we can change the color and text based on the flavors. So is important that we get the edible design for front and back of the packages and sachets. Each package contains 10 small sachets where the design of the sachets should be a similar design as the packages itself.

I will provide an example picture/template (just a guideline, not obligatory) from the factory and the sachets, but also from our competitors. Is important that both packaging design and sachets design is editable from both sides if we in the future add new flavors or text.

I will also provide a word file with the necessary text on the pack of the packaging and Nutrition Facts for both of the two flavors. Important that the ingredients are a least in both Norwegian (N) and English (GB). The word file also contains the company information, put on the back of the packaging.

Attached pls find two pictures of design template. Maybe you need them when designing. It's the dimension of 10 sachets/box and 0.6g/sachet the factory use. Our logo BrimLeaf should be on the packaging and the sachets. I also provided the logo in editable format.

Brim Instant Lemon:
GB Ingredients : Lemon, black tea
N Ingredienser: Sitron, svart te

Brim Instant Hibiscus:
GB Ingredients: Hibiscus, rose, black tea and stevia extract
N Ingredienser: Hibiscus, rose, svart te og stevia ekstrakt

Experience the new generation of tea! BrimLeaf® is one of the world fist premium instant tea. Made from real fruit and whole tea leaf, you get incredible tea in seconds. Based on patented cold-brewed technology provide you with the essence of tea, without the need for sugar or preservatives. Brim with health, Brim with taste!

Distributed by Korvenet AS®
PO BOX: 4027
Oslo, Mørkedalsgata 5, Norway
Learn more at BrimLeaf.example

Hope your design can help us stand out from the crowd.

With best regards,

Torvald
CEO of Korvenet As

Target Market(s)

The beverages market, or more correctly the tea market.
The product is Premium Instant Tea.

Font styles to use
Serif

Colors

Designer to choose colors to be used in the design.

Requirements
Must have
• The name of the tea flavor in its representative color.
• Brim Instant Lemon
• Premium Black tea (Smaller letters)
• Brim Instant Hibiscus
• Premium Herbal Tea (Smaller letters)
• General facts:
• * 100 % Natural, no additives, artificial flavors or preventative.
• * 0 fat/ 0 Sugar / 0 Calories.
• * In Crystal instead of tea powder or tea bag.
• * It is soluble in 3 seconds with 200 ml to 300 ml hot or cold pure water.
• Looking for a design where we can change the color and text based on the different flavors. So is important that we get the edible design for the and back of the packages and sachets.
• Ingredients in Norwegian (N) and English(GB) and nutrition values in Norwegian and if possible in English. Remember the company information (provided in the packeging.docx) at the back with a link to our website, www.BrimLeaf.example.
• Must show how the product works on the front and the back. Remember instant tea in 3 seconds from sachets. 10 sachets in each pack, should be a part of the front information, see provided examples.
• Important that we can easily change it our self with affinity or other programs, based on new text or flavor. So we need 360-degree design, so we can change the back and the front, based on what our factory can print out.
• Remember that the design should be reused many times, not just for one of those two flavors above. Simple, but yet elegant and upmarket.
• Each package contains 10 small sachets where the design of the sachets should be a similar design as the packages itself. I will provide an example picture/template from the factory and the sachets, but also from our competitors.
• Is important that both packaging design and sachets design is editable from both sides if we in the future add new flavors or text. I will also provide a word file with the necessary text on the pack of the packaging and Nutrition Facts for both of the two flavors. Important that the ingredients are a least in both Norwegian (N) and English (GB). The word file also contains the company information, put on the back of the packaging.
• Brim Lemon:
• GB Ingredients: Lemon, black tea
• N Ingredienser: Sitron, svart te
• Brim Hibiscus:
• GB Ingredients: Hibiscus, rose, black tea and stevia extract
• N Ingredienser: Hibiscus, rose, svart te og stevia ekstrakt
• Text on the back:
• Experience the new generation of tea! BrimLeaf® is one of the world fist premium instant tea. Made from real fruit and whole tea leaf, you get incredible tea in seconds. Based on patented cold-brewed technology provide you with the essence of tea, without the need for sugar or preservatives. Brim with health, Brim with taste!
• Company information:
• Distributed by Korvenet AS®
• PO BOX: 4027
• Oslo, Mørkedalsgata 5, Norway
• Learn more at www.BrimLeaf.example
Nice to have
• Take a look at Bemo Tea, Vardy Tea and Hollet.
• Especially Hollet since they have a clean and high-class design. https://www.holletleaf.example/tea-by-type/indian-breakfast-25-tea-bags?___SID=U.
• Nice with ® on top of the A on BrimLeaf logo.
• Quiro has also nice designs: https://www.quiroleaf.example/us/en/products/hot.html
• Remember the sticking out / eye-catcher". For both of these proposals, I think that if it had some gold elements in the same way that Sundmark coffee has (a little more expensive for flavor) and that the white color of the proposal one is replaced by light black on the sides and either black or gold in the field where the text. In other words, I think that the packaging should be as identical as possible regardless of taste.
• Feedback for Manufacturer: (Just suggestion from her)
• About the packaging, my suggestion is as follows:
• 1) I think color should match "lemon black tea".We'd better choose the color which in coordination with the flavor, for customer's observation conveniently.
• 2) As for the phrase "cold water instant tea", I think it'd better we remark "stir or shake for better dissolving" or similar meanings in the package. Or describing it by pattern as the attachment FYI. Because these two flavors contain black tea which has enzyme. The molecule of enzyme is a little bigger, so it's a little hard to be totally dissolved by cold water without stirring or shaking.
• Pure tea in hot or cold pure water for you anytime, everywhere on the go (On the back
Should not have
• We hate Parvel, Ashcombe's design. Remember simple, modern and elegant. We are the future of tea, don't make your grandma happy with the design!
• Please avoid using teacups in the design!
• Best regards,
• Torvald

```html
<!DOCTYPE html>
<html lang="en">
<head>
<meta charset="utf-8">
<title>BrimLeaf – Brim Lemon Black Tea box dieline</title>
<link rel="stylesheet" href="https://fonts.googleapis.com/css2?family=Cinzel:wght@700&family=Lato:wght@400;700&family=Roboto+Condensed:wght@400;700&family=Libre+Baskerville:wght@700&display=swap">
<style>
  :root{
    --paper:#ffffff;
    --flap:#d4d5d7;
    --sun-light:#fff6b8;
    --sun:#ffd21e;
    --amber:#f7a928;
    --orange:#ef8a1f;
    --ink:#1b1b1b;
    --brown:#5b3a0e;
    --copy:#4a3208;
    --label:#232a36;
  }
  *{box-sizing:border-box;margin:0;padding:0}
  html,body{width:1200px;height:850px;overflow:hidden;background:var(--paper)}
  .dieline{position:relative;width:1200px;height:850px}
  .dieline svg.flaps{position:absolute;inset:0}
  .panel{position:absolute;top:164px;height:522px;overflow:hidden}
  .panel--back{left:110px;width:384px;
    background:linear-gradient(180deg,var(--sun-light) 0%,var(--sun) 38%,var(--amber) 72%,var(--orange) 100%)}
  .panel--side{width:120px;
    background:linear-gradient(180deg,var(--sun-light) 0%,var(--sun) 40%,var(--amber) 75%,var(--orange) 100%)}
  .panel--side-left{left:494px}
  .panel--side-right{left:998px}
  .panel--front{left:614px;width:384px;
    background:radial-gradient(circle at 50% 14%,#fffdf0 0%,var(--sun-light) 18%,var(--sun) 48%,var(--amber) 80%,var(--orange) 100%)}
  .fold-frame{position:absolute;left:494px;top:164px;width:626px;height:522px;border:2px solid var(--ink);pointer-events:none}
  .fold-frame::before,.fold-frame::after{content:"";position:absolute;top:0;bottom:0;width:2px;background:var(--ink)}
  .fold-frame::before{left:118px}
  .fold-frame::after{left:502px}

  /* nutrition */
  .nutrition{position:absolute;left:16px;top:18px;width:163px;height:362px;background:var(--ink);padding:3px}
  .nutrition__inner{border:2px solid #fff;height:100%;padding:8px 8px 6px;color:#fff;
    font-family:"Roboto Condensed",sans-serif;font-size:9.4px;line-height:1}
  .nutrition h2{font-size:17px;font-weight:700;letter-spacing:-.2px;padding-bottom:3px;border-bottom:1px solid #fff}
  .nutrition .servings{padding-top:3px}
  .nutrition .serving-size{font-weight:700;padding:2px 0 3px;border-bottom:4px solid #fff}
  .nutrition .amount{font-size:6px;padding-top:4px}
  .nutrition .calories{display:flex;justify-content:space-between;align-items:flex-end;font-weight:700;font-size:12px;padding-bottom:2px;border-bottom:3px solid #fff}
  .nutrition .calories b{font-size:18px}
  .nutrition .dv{text-align:right;font-size:6px;font-weight:700;padding:4px 0 3px;border-bottom:1px solid #fff}
  .nutrition .row{display:flex;justify-content:space-between;padding:4px 0 3px;border-bottom:1px solid #fff}
  .nutrition .row span:last-child{font-weight:700}
  .nutrition .indent{padding-left:7px}
  .nutrition .indent2{padding-left:15px}
  .nutrition .thick{border-bottom:4px solid #fff}
  .nutrition .last{border-bottom:none}

  .back-copy{position:absolute;left:188px;top:24px;width:180px;font-family:"Lato",sans-serif;color:var(--copy);font-weight:700}
  .back-copy h3{font-size:13.5px;font-weight:700;margin-bottom:3px;color:#3d2a08}
  .back-copy p{font-size:11.3px;line-height:13.6px}
  .back-copy .section{padding-bottom:8px;border-bottom:2px solid #3d2a08;margin-bottom:11px}
  .back-copy .company{font-size:11.3px;line-height:13.6px}
  .back-facts{position:absolute;left:27px;top:409px;font-family:"Lato",sans-serif;font-weight:700;color:var(--brown);font-size:13.6px;line-height:17.5px}
  .back-facts p+p{margin-top:16px}
  .back-facts .caps{text-transform:uppercase}
  .print-block{position:absolute;left:215px;top:413px;width:140px;height:70px;background:#fff}

  /* front */
  .brand{position:absolute;left:0;right:0;top:86px;display:flex;justify-content:center;align-items:center;gap:8px}
  .brand__dot{width:12px;height:12px;border-radius:50%;background:#2e2a24}
  .brand__name{font-family:"Lato",sans-serif;font-weight:700;font-size:27px;color:#2e2a24}
  .flavour{position:absolute;left:0;right:0;top:200px;text-align:center;font-family:"Cinzel",serif;font-weight:700;
    font-size:29px;line-height:36px;color:#2a2115;letter-spacing:.5px}
  .serving-visual{position:absolute;left:6px;top:336px;width:264px;height:186px;
    background:linear-gradient(180deg,rgba(255,255,255,.35) 0%,#b9391b 30%,#c85a1c 60%,#e4f0d8 82%,#f3f5ef 100%);
    border-radius:6px 6px 0 0}
  .flavour-tag{position:absolute;left:272px;top:444px;width:88px;height:78px}
  .flavour-tag span{position:absolute;left:0;right:0;top:31px;text-align:center;font-family:"Libre Baskerville",serif;
    font-weight:700;font-size:11.5px;line-height:15px;color:#fff}
</style>
</head>
<body>
<div class="dieline">
  <svg class="flaps" width="1200" height="850" viewBox="0 0 1200 850" aria-hidden="true">
    <g fill="var(--flap)">
      <rect x="110" y="44" width="384" height="120"/>
      <rect x="614" y="44" width="384" height="120"/>
      <path d="M494 164 V72 Q494 50 516 50 H592 Q614 50 614 72 V164 Z"/>
      <path d="M998 164 V72 Q998 50 1020 50 H1096 Q1118 50 1118 72 V164 Z"/>
      <rect x="110" y="686" width="384" height="120"/>
      <rect x="614" y="686" width="384" height="120"/>
      <path d="M494 686 V778 Q494 800 516 800 H592 Q614 800 614 778 V686 Z"/>
      <path d="M998 686 V778 Q998 800 1020 800 H1096 Q1118 800 1118 778 V686 Z"/>
      <path d="M110 164 L80 178 V672 L110 686 Z"/>
    </g>
  </svg>

  <section class="panel panel--back">
    <div class="nutrition">
      <div class="nutrition__inner">
        <h2>Nutrition Facts</h2>
        <div class="servings">10 servings per container</div>
        <div class="serving-size">Serving size1 tea-stick (1.2g)</div>
        <div class="amount">Amount Per Serving</div>
        <div class="calories">Calories <b>0</b></div>
        <div class="dv">% Daily Value*</div>
        <div class="row"><span><b>Total Fat</b> 0g</span><span>0%</span></div>
        <div class="row indent"><span>Saturated Fat 0g</span><span>0%</span></div>
        <div class="row indent"><span><i>Trans</i> Fat 0g</span><span></span></div>
        <div class="row"><span><b>Cholesterol</b> 0mg</span><span>0%</span></div>
        <div class="row"><span><b>Sodium</b> 0g</span><span>0%</span></div>
        <div class="row"><span><b>Total Carbohydrate</b> 0g</span><span>0%</span></div>
        <div class="row indent"><span>Dietary Fiber 0g</span><span>0%</span></div>
        <div class="row indent"><span>Total Sugars 0g</span><span></span></div>
        <div class="row indent2"><span>Includes 0g Added Sugars</span><span>0%</span></div>
        <div class="row thick"><span><b>Protein</b> 0g</span><span></span></div>
        <div class="row"><span>Vitamin D 0mg</span><span>0%</span></div>
        <div class="row"><span>Calcium 0mg</span><span>0%</span></div>
        <div class="row"><span>Iron 0mg</span><span>0%</span></div>
        <div class="row last"><span>Potassium 0mg</span><span>0%</span></div>
      </div>
    </div>

    <div class="back-copy">
      <div class="section">
        <h3>Caffeine Content:</h3>
        <p>Experience the new generation of tea! BrimLeaf® is one of the world fist premium instant tea. Made from real fruit and whole tea leaf, you get incredible tea in seconds. Based on patented cold-steep technology provide you the essence of tea, without the need for sugar or preservatives. Brim with health, Brim with taste!</p>
      </div>
      <div class="section">
        <h3>Instruction for use:</h3>
        <p>Lorem ipsum dolor sit amet, consectetuer adipiscing elit, sed diam nonummy nibh euismod tincidunt ut laoreet dolore magna aliquam erat volutpat. Ut wisi enim ad minim veniam.</p>
      </div>
      <p class="company">Distributed by Korvenet AS®<br>PO BOX: 4027<br>Oslo, Mørkedalsgata 5, Norway<br>Learn more at BrimLeaf.example</p>
    </div>

    <div class="back-facts">
      <p>Tea Polyphenols<br>190mg par serving</p>
      <p><span class="caps">Ingredients:</span><br>Organic Black Tea, Lemon</p>
    </div>
    <div class="print-block"></div>
  </section>

  <section class="panel panel--side panel--side-left"></section>

  <section class="panel panel--front">
    <div class="brand">
      <span class="brand__dot"></span>
      <span class="brand__name">BrimLeaf</span>
    </div>
    <h1 class="flavour">Brim Lemon<br>Black Tea</h1>
    <div class="serving-visual" role="img" aria-label="Photo of a glass cup of amber black tea on a saucer with a lime slice and an orange slice"></div>
    <div class="flavour-tag">
      <svg width="88" height="78" viewBox="0 0 88 78" aria-hidden="true"><path d="M0 0 L44 12 L88 0 V78 H0 Z" fill="var(--label)"/></svg>
      <span>Lemon<br>BlackTea</span>
    </div>
  </section>

  <section class="panel panel--side panel--side-right"></section>

  <div class="fold-frame"></div>
</div>
</body>
</html>
```